HRW / PFB

I need a business card for the owner of sister companies. Please see minimalist version of our old business card for just the Halvorsen business. We need to now have a card that shows off both the Halvorsen logo and the Pale Fern Builders logo. We would like the aesthetic to go well with our brand, and not differ greatly from our Halvorsen cards. These companies are sister companies, there is not one parent company. Looking for a visually appealing design, but not sure if it should be diagonal or something to make it visually attractive... or just some other type of divider. We prefer white logos with a blue background. White transparent background png logos are attached. Please use blue background with hex code 566b7c. The person and contact information will be on the back side, and I can do that myself. We will NOT need to add the text for design-build-sales-installation.

```html
<!DOCTYPE html>
<html lang="en">
<head>
<meta charset="utf-8">
<title>HRW / PFB Business Card</title>
<link rel="stylesheet" href="https://fonts.googleapis.com/css2?family=Montserrat:wght@400;500;600;700&display=swap">
<style>
  :root {
    --brand-blue: #566b7c;
    --card-white: #ffffff;
    --stage: #3a3a3c;
    --stripe-grey: #a9b3bc;
    --rule: #566b7c;
  }
  * { box-sizing: border-box; margin: 0; padding: 0; }
  html, body { width: 1200px; height: 1200px; overflow: hidden; }
  body {
    background: var(--stage);
    font-family: "Montserrat", sans-serif;
    position: relative;
  }
  .card {
    position: absolute;
    left: 250px;
    width: 700px;
    height: 400px;
    border-radius: 32px;
    overflow: hidden;
  }
  .card-front { top: 150px; background: var(--card-white); }
  .card-back { top: 650px; background: var(--brand-blue); }

  .front-band { position: absolute; inset: 0; }

  .brand-row {
    position: absolute;
    display: flex;
    align-items: center;
    gap: 34px;
  }
  .card-front .brand-row { left: 160px; top: 80px; }
  .card-back .brand-row { left: 0; right: 0; top: 170px; justify-content: center; }

  .brand { display: flex; align-items: center; gap: 12px; font-weight: 600; }
  .brand-mark { width: 34px; height: 34px; }
  .card-front .brand { color: var(--brand-blue); font-size: 24px; }
  .card-front .brand-mark { border: 4px solid var(--brand-blue); }
  .card-back .brand { color: var(--card-white); font-size: 30px; }
  .card-back .brand-mark { border: 5px solid var(--card-white); width: 42px; height: 42px; }

  .header-rule {
    position: absolute;
    left: 160px; right: 60px; top: 145px;
    height: 1px; background: var(--rule);
  }

  .identity { position: absolute; left: 62px; top: 212px; color: var(--brand-blue); }
  .identity .full-name { font-size: 34px; font-weight: 700; letter-spacing: 0.5px; }
  .identity .title { font-size: 17px; font-weight: 500; color: #444; margin-top: 2px; letter-spacing: 1px; }
  .identity .divider { width: 300px; height: 1px; background: #555; margin: 10px 0 12px; }
  .contact { list-style: none; font-size: 20px; color: #333; }
  .contact li { display: flex; align-items: center; gap: 12px; line-height: 30px; }
  .contact svg { width: 20px; height: 20px; fill: var(--brand-blue); }

  .website {
    position: absolute; right: 40px; top: 336px;
    color: var(--card-white); font-size: 20px; letter-spacing: 0.5px;
    white-space: nowrap;
  }
</style>
</head>
<body>
  <section class="card card-front">
    <svg class="front-band" viewBox="0 0 700 400" aria-hidden="true">
      <path d="M0,362 L330,362 C380,362 390,292 455,292 L700,292 L700,300 L455,300 C395,300 385,370 330,370 L0,370 Z" fill="var(--stripe-grey)"/>
      <path d="M0,372 L330,372 C382,372 392,302 455,302 L700,302 L700,400 L0,400 Z" fill="var(--brand-blue)"/>
    </svg>
    <div class="brand-row">
      <div class="brand"><span class="brand-mark"></span>Halvorsen</div>
      <div class="brand">Pale Fern Builders</div>
    </div>
    <div class="header-rule"></div>
    <div class="identity">
      <div class="full-name">FULL NAME</div>
      <div class="title">TITLE</div>
      <div class="divider"></div>
      <ul class="contact">
        <li><svg viewBox="0 0 24 24"><path d="M6.6 10.8a15.1 15.1 0 0 0 6.6 6.6l2.2-2.2a1 1 0 0 1 1-.25 11.4 11.4 0 0 0 3.6.57 1 1 0 0 1 1 1V20a1 1 0 0 1-1 1A17 17 0 0 1 3 4a1 1 0 0 1 1-1h3.5a1 1 0 0 1 1 1c0 1.25.2 2.45.57 3.570a1 1 0 0 1-.25 1z"/></svg>(000) 000 0000</li>
        <li><svg viewBox="0 0 24 24"><path d="M2 5h20v14H2z M3.5 6.5 12 13l8.5-6.5" fill="none" stroke="var(--brand-blue)" stroke-width="2"/></svg>email@company.com</li>
      </ul>
    </div>
    <div class="website">www.company.com</div>
  </section>

  <section class="card card-back">
    <div class="brand-row">
      <div class="brand"><span class="brand-mark"></span>Halvorsen</div>
      <div class="brand">Pale Fern Builders</div>
    </div>
  </section>
</body>
</html>
```